■依頼の目的/概要
ビジネス本の表紙デザインをお願いします。

■本の内容
・起業初期の起業家、または副業で月収入10万円UPしたい方向けの、
77のWEBのアドバイス(テクニック)をまとめた本です。

■デザイン要望
どちらかというと、30~50代女性起業家向けです。
女性のイラストが入ると嬉しいです。

その他何かご不明な点がございましたら、お気軽にご質問下さい。
よろしくお願いいたします。

■プレセントの記載をお願いします。
①何が足りないかすぐ分かる!
WEBチェックシート

②1年で1万人フォロワーを達成した
Plumoraフォロワー増やしのコツ

③最短で成功へ向かう無料コンサル

女性らしい優しい雰囲気で、誰からも愛されるデザインと感じました。

この度はご応募頂き、誠にありがとうございました!

どのデザインも素敵で、本当に迷いました。
修正していただいた方には、親切に対応して頂き心より感謝しております。

皆様の益々のご活躍を祈念しております。
今回は本当に有難うございました。

```html
<!DOCTYPE html>
<html lang="ja">
<head>
<meta charset="UTF-8">
<title>知っておくべきWEBテクニック77のポイント</title>
<link rel="stylesheet" href="https://fonts.googleapis.com/css2?family=M+PLUS+Rounded+1c:wght@500;700;800&family=Yomogi&display=swap">
<style>
  :root {
    --bg-pink: #f3a79e;
    --band-pink: #e9867d;
    --frame-white: #fffaf6;
    --ink: #3b3535;
    --accent: #e67f74;
    --yellow: #f7d865;
    --white: #ffffff;
  }
  * { margin: 0; padding: 0; box-sizing: border-box; }
  html, body { width: 750px; height: 1200px; overflow: hidden; background: var(--bg-pink); }
  .cover {
    position: relative; width: 750px; height: 1200px; overflow: hidden;
    background: var(--bg-pink);
    font-family: "M PLUS Rounded 1c", sans-serif; color: var(--ink);
  }
  .icon-pattern {
    position: absolute; inset: 0 0 320px 0;
    background: linear-gradient(160deg, #f5b2a9 0%, #f1a196 100%);
  }
  .tagline {
    position: absolute; left: 30px; top: 28px; width: 600px;
    font-family: "Yomogi", sans-serif; color: var(--ink);
    transform: rotate(-4deg); transform-origin: left top;
  }
  .tagline .monthly { font-size: 30px; font-weight: 700; display: block; margin-left: 20px; font-family: "M PLUS Rounded 1c", sans-serif; }
  .tagline .amount { font-size: 52px; }
  .tagline .up { font-size: 52px; }
  .tagline .rest { font-size: 32px; }
  .title-frame {
    position: absolute; left: 112px; top: 212px; width: 526px; height: 430px;
    background: var(--frame-white); border-radius: 60px;
    box-shadow: 0 0 0 6px rgba(255,255,255,0.5);
  }
  .frame-line { position: absolute; left: 112px; top: 212px; }
  .title { position: absolute; left: 112px; width: 526px; text-align: center; }
  .title-lead { top: 255px; font-size: 36px; font-weight: 700; }
  .title-lead::after {
    content: ""; display: block; width: 320px; height: 3px; margin: 10px auto 0;
    background: var(--accent);
  }
  .title-main { top: 330px; font-size: 104px; font-weight: 800; letter-spacing: 4px; line-height: 1; }
  .title-sub { top: 458px; font-size: 90px; font-weight: 800; line-height: 1; }
  .points-pill {
    position: absolute; left: 222px; top: 612px; width: 306px; height: 72px;
    background: var(--yellow); border-radius: 36px;
    font-size: 38px; font-weight: 800; color: var(--accent);
    display: flex; align-items: center; justify-content: center; white-space: nowrap;
  }
  .points-pill b { font-size: 50px; font-style: italic; margin-right: 2px; }
  .author {
    position: absolute; left: 48px; top: 730px; font-size: 38px; font-weight: 700;
  }
  .author small { font-size: 22px; font-weight: 500; margin-left: 6px; }
  .illustration {
    position: absolute; left: 450px; top: 700px; width: 290px; height: 180px;
    border-radius: 145px 145px 20px 20px;
    background: linear-gradient(180deg, #fbe3d8 0%, #c9d3e6 100%);
  }
  .gift-band {
    position: absolute; left: 0; top: 880px; width: 750px; height: 320px;
    background: var(--band-pink);
  }
  .gift-heading {
    position: absolute; left: 48px; top: 900px;
    font-size: 38px; font-weight: 800; color: var(--white);
    padding-bottom: 6px; border-bottom: 3px solid var(--white);
  }
  .gift-list { position: absolute; left: 44px; top: 972px; width: 680px; list-style: none; }
  .gift-item { display: flex; align-items: center; gap: 14px; margin-bottom: 14px; color: var(--white); font-weight: 700; }
  .gift-num {
    flex: none; width: 40px; height: 44px; background: var(--yellow);
    color: var(--accent); font-size: 32px; font-weight: 800;
    display: flex; align-items: center; justify-content: center;
  }
  .gift-text { font-size: 29px; line-height: 1.2; }
  .gift-text small { display: block; font-size: 20px; font-weight: 500; }
</style>
</head>
<body>
<div class="cover">
  <div class="icon-pattern" role="img" aria-label="淡いWEBアイコン柄の背景"></div>

  <p class="tagline">
    <span class="monthly">毎月収入</span>
    <span class="amount">10万円</span><span class="up">UP</span><span class="rest">したいあなたに贈る!</span>
  </p>

  <div class="title-frame"></div>
  <svg class="frame-line" width="526" height="430" viewBox="0 0 526 430" aria-hidden="true">
    <rect x="16" y="16" width="494" height="398" rx="48" fill="none" stroke="#e67f74" stroke-width="2"/>
  </svg>

  <p class="title title-lead">知っておくべき</p>
  <h1 class="title title-main">WEB</h1>
  <p class="title title-sub">テクニック</p>
  <p class="points-pill"><b>77</b>のポイント</p>

  <p class="author">花村 さやか<small>[著]</small></p>

  <div class="illustration" role="img" aria-label="ノートパソコンに向かう女性のイラスト"></div>

  <div class="gift-band"></div>
  <h2 class="gift-heading">読者プレゼント</h2>
  <ol class="gift-list">
    <li class="gift-item"><span class="gift-num">1</span><span class="gift-text"><small>何が足りないかすぐ分かる!</small>WEB チェックシート</span></li>
    <li class="gift-item"><span class="gift-num">2</span><span class="gift-text"><small>1年で1万人フォロワーを達成した</small>Plumoraフォロワー増やしのコツ</span></li>
    <li class="gift-item"><span class="gift-num">3</span><span class="gift-text">最短で成功へ向かう無料コンサル</span></li>
  </ol>
</div>
</body>
</html>
```